Unique and original Business Card for Financial Services Business

I have moved premises and need to change the detail on my business card so thought now is a good time for a re-design. Looking for something professional and modern with colours to fit in with out logo. Like the idea of foil or embossing if that works but not a must have but I do want something that stands out and that I could not design myself.

Once business card is designed I will also be looking to get letterhead and flyers done but want the business card concept in place first.

The majority of designs I am receiving are generic and template based. I am looking for something unique and original. We have some great design elements in our logo, think outside the box and show me something that stands out from the crowd.

Target Market(s)

Business Professionals

Industry/Entity Type

Finance

Contact Information for Business Card

Name: Delia Norwood Phone 0473 958 162 Address PO Box 8617 Mossvale NSW 2389 Email info@steadyharbourfinancialservices.com.au website www.steadyharbourfinancialservices.com.au

Font styles to use
Other font styles liked:
• Ralway

Requirements
Should not have
• No black backgrounds please

```html
<!DOCTYPE html>
<html lang="en">
<head>
<meta charset="utf-8">
<title>Steady Harbour Financial Services – Business Card</title>
<link rel="stylesheet" href="https://fonts.googleapis.com/css2?family=Open+Sans:wght@400;700&family=Raleway:wght@300;400&display=swap">
<style>
  :root {
    --stage: #3b3b3b;
    --card: #263236;
    --card-shade: #1f292c;
    --card-light: #34454a;
    --teal: #2b8fa0;
    --teal-light: #5cbccc;
    --text: #eef2f3;
    --text-soft: #c3ced1;
    --rule: #3f8693;
  }
  * { box-sizing: border-box; margin: 0; padding: 0; }
  html, body { width: 1200px; height: 801px; overflow: hidden; }
  body {
    background: var(--stage);
    display: flex;
    align-items: center;
    justify-content: center;
    gap: 40px;
    font-family: "Open Sans", Arial, sans-serif;
  }
  .card {
    width: 540px;
    height: 309px;
    background: var(--card);
    border-bottom: 3px solid var(--teal);
    position: relative;
    overflow: hidden;
  }

  /* Front */
  .card-front { display: flex; align-items: center; padding-left: 20px; }
  .brand {
    width: 250px;
    display: flex;
    flex-direction: column;
    align-items: center;
    gap: 8px;
  }
  .brand-row { display: flex; align-items: center; gap: 9px; }
  .brand-mark { width: 20px; height: 20px; background: var(--teal); flex: none; }
  .brand-name {
    font-family: "Raleway", Arial, sans-serif;
    font-weight: 300;
    font-size: 21px;
    letter-spacing: 0.5px;
    color: var(--teal-light);
    text-transform: uppercase;
    white-space: nowrap;
  }
  .brand-tag {
    font-family: "Raleway", Arial, sans-serif;
    font-weight: 300;
    font-size: 12px;
    letter-spacing: 4px;
    color: var(--text-soft);
    white-space: nowrap;
  }
  .divider { width: 1px; height: 170px; background: var(--rule); margin-left: 10px; }
  .contact { padding-left: 18px; color: var(--text); }
  .contact-name {
    font-weight: 700;
    font-size: 19px;
    color: var(--teal-light);
    text-transform: uppercase;
    letter-spacing: 0.5px;
  }
  .contact-role { font-size: 12.5px; margin-bottom: 11px; color: var(--text-soft); }
  .contact-address { font-size: 12px; line-height: 1.45; margin-bottom: 11px; }
  .contact-list { list-style: none; font-size: 10px; line-height: 1.9; }
  .contact-list li { display: flex; align-items: center; gap: 6px; white-space: nowrap; }
  .contact-list svg { width: 10px; height: 10px; flex: none; fill: var(--teal-light); }

  /* Back */
  .card-back .pattern {
    position: absolute; inset: 0;
    background:
      radial-gradient(ellipse at 80% 55%, rgba(92,188,204,0.10) 0%, rgba(92,188,204,0) 45%),
      linear-gradient(115deg, var(--card-shade) 0%, var(--card) 45%, var(--card-light) 100%);
  }
  .back-mark {
    position: absolute;
    right: 52px;
    top: 150px;
    display: flex;
    align-items: center;
    gap: 7px;
  }
  .back-mark .brand-mark { width: 16px; height: 16px; }
  .back-mark span {
    font-family: "Raleway", Arial, sans-serif;
    font-weight: 300;
    font-size: 14px;
    color: var(--teal-light);
    text-transform: uppercase;
    letter-spacing: 1px;
  }
</style>
</head>
<body>
  <section class="card card-front">
    <div class="brand">
      <div class="brand-row">
        <span class="brand-mark"></span>
        <span class="brand-name">Steady Harbour</span>
      </div>
      <span class="brand-tag">Financial Services</span>
    </div>
    <div class="divider"></div>
    <div class="contact">
      <p class="contact-name">Delia Norwood</p>
      <p class="contact-role">President</p>
      <p class="contact-address">PO Box 8617<br>Mossvale NSW 2389</p>
      <ul class="contact-list">
        <li><svg viewBox="0 0 24 24"><path d="M6.6 10.8a15 15 0 0 0 6.6 6.6l2.2-2.2a1 1 0 0 1 1-.25 11.4 11.4 0 0 0 3.6.57 1 1 0 0 1 1 1V20a1 1 0 0 1-1 1A17 17 0 0 1 3 4a1 1 0 0 1 1-1h3.5a1 1 0 0 1 1 1 11.4 11.4 0 0 0 .57 3.6 1 1 0 0 1-.25 1z"/></svg>0473 958 162</li>
        <li><svg viewBox="0 0 24 24"><path d="M2 5h20v14H2zm2 2v.5l8 5 8-5V7l-8 5z"/></svg>info@steadyharbourfinancialservices.com.au</li>
        <li><svg viewBox="0 0 24 24"><circle cx="12" cy="12" r="10"/></svg>www.steadyharbourfinancialservices.com.au</li>
      </ul>
    </div>
  </section>

  <section class="card card-back">
    <div class="pattern" role="img" aria-label="Tonal repeating emblem pattern in spot gloss across the whole card back"></div>
    <div class="back-mark">
      <span class="brand-mark"></span>
      <span>Steady Harbour</span>
    </div>
  </section>
</body>
</html>
```